Boutique Barre Studio in Geneva

Business card for pilates and dance studio. We are a brand new studio and love our fresh image with our yellow color. This business card is meant for our founder.

```html
<!DOCTYPE html>
<html lang="en">
<head>
<meta charset="utf-8">
<title>Arcline Studio – Business Card</title>
<link href="https://fonts.googleapis.com/css2?family=Open+Sans:ital,wght@0,300;0,400;1,400&display=swap" rel="stylesheet">
<style>
  :root {
    --page-bg: #d9d6d1;
    --card-bg: #efeeeb;
    --brand-yellow: #dcc640;
    --circle-yellow: #e3cd3c;
    --ink: #3a3d42;
    --ink-soft: #55585d;
  }
  html, body {
    margin: 0;
    padding: 0;
    width: 1200px;
    height: 1054px;
    overflow: hidden;
    background: var(--page-bg);
    font-family: "Open Sans", Arial, sans-serif;
  }
  .card {
    position: absolute;
    left: 100px;
    top: 224px;
    width: 1000px;
    height: 606px;
    background: var(--card-bg);
    border-radius: 20px;
    overflow: hidden;
    box-shadow: 0 10px 30px rgba(0,0,0,0.12);
  }
  .accent-circle {
    position: absolute;
    left: 447px;
    top: 25px;
    width: 560px;
    height: 560px;
    border-radius: 50%;
    background: var(--circle-yellow);
    opacity: 0.85;
  }
  .brand {
    position: absolute;
    left: 40px;
    top: 48px;
    color: var(--brand-yellow);
    font-weight: 300;
    line-height: 1;
  }
  .brand-name {
    display: block;
    font-size: 96px;
    letter-spacing: -1px;
  }
  .brand-sub {
    display: block;
    font-size: 30px;
    letter-spacing: 4px;
    margin-left: 60px;
    margin-top: 2px;
  }
  .person-name {
    position: absolute;
    left: 42px;
    top: 258px;
    margin: 0;
    font-size: 34px;
    font-weight: 400;
    color: var(--ink);
  }
  .person-role {
    position: absolute;
    left: 42px;
    top: 308px;
    margin: 0;
    font-size: 22px;
    font-style: italic;
    color: var(--ink-soft);
  }
  .address {
    position: absolute;
    left: 42px;
    top: 368px;
    margin: 0;
    font-style: normal;
    font-size: 24px;
    line-height: 39px;
    color: var(--ink-soft);
  }
  .contact-list {
    position: absolute;
    left: 42px;
    top: 455px;
    margin: 0;
    padding: 0;
    list-style: none;
    font-size: 24px;
    color: var(--ink-soft);
  }
  .contact-item {
    display: flex;
    align-items: center;
    height: 40px;
  }
  .contact-icon {
    width: 24px;
    height: 24px;
    margin-right: 28px;
    stroke: var(--brand-yellow);
    fill: none;
    stroke-width: 1.8;
  }
</style>
</head>
<body>
  <div class="card">
    <div class="accent-circle"></div>

    <div class="brand">
      <span class="brand-name">arcline</span>
      <span class="brand-sub">STUDIO</span>
    </div>

    <h1 class="person-name">Mara Lindqvist</h1>
    <p class="person-role">Founder</p>

    <address class="address">RUE DES Pâquis 18 1201<br>Geneva, Switzerland</address>

    <ul class="contact-list">
      <li class="contact-item">
        <svg class="contact-icon" viewBox="0 0 24 24"><circle cx="12" cy="12" r="10"/><path d="M8.5 7.5c0 4.5 3.5 8 8 8l1-2-2.5-1-1 1c-1.5-.6-2.9-2-3.5-3.5l1-1-1-2.5z"/></svg>
        +33 700482615
      </li>
      <li class="contact-item">
        <svg class="contact-icon" viewBox="0 0 24 24"><rect x="3" y="6" width="18" height="12" rx="1"/><path d="M3 6l9 7 9-7"/></svg>
        hello@arcline-studio.com
      </li>
      <li class="contact-item">
        <svg class="contact-icon" viewBox="0 0 24 24"><circle cx="12" cy="12" r="10"/><ellipse cx="12" cy="12" rx="4" ry="10"/><path d="M2 12h20"/></svg>
        www.arcline-studio.com
      </li>
    </ul>
  </div>
</body>
</html>
```